Digital marketing agency needs a new website design

We need a new responsive design for our website: https://brivolta.com/

Brivolta is a french digital marketing company who specializes in helping companies rank higher on Quendo search engine for their keywords in order to be more visible and have more traffic and clients.

I need you to design these 5 pages:
- Home page: https://brivolta.com
- Pricing page: https://brivolta.com/packs-backlinks/
- Contact page: https://brivolta.com/contact/
- Thank you page: https://brivolta.com/merci-temp/
- Simple page : https://brivolta.com/a-propos/

Here is a list of websites that we like their design. Use it for inspiration, but make sure it is different :

https://fenrolt.io/ (this is the one I like the most)
https://ubro.com/
http://www.garvelnest.com/
https://lumbardeau.fr/
https://www.tressaplank.com/home
https://dovermick.com/fr/
https://kalvoxa.io/
https://tramoisenet.fr/

I want a 75% color background and 25% white. You should use many bright/pastel colors like this website : https://fenrolt.io/

Keep the contact form in the website header.

Target Market(s)

small business owners

Industry/Entity Type

Digital Marketing

Number of Pages Required

5+ page

Font styles to use
Sans Serif

Colors

Designer to choose colors to be used in the design.

Requirements
Must have
• Contact form in header.
• Prominent call-to-action buttons.
• Use of at least 1 flashy color, possible to use many.
• Keep the 3 chart images.
• Keep client testimonials

```html
<!DOCTYPE html>
<html lang="fr">
<head>
<meta charset="utf-8">
<title>Brivolta – Backlinks français</title>
<link href="https://fonts.googleapis.com/css2?family=Raleway:wght@600;700;800&family=Open+Sans:wght@400;600;700&display=swap" rel="stylesheet">
<style>
:root{
  --violet:#5a16d8;
  --magenta:#d81aa8;
  --pink:#f0136f;
  --blue:#0a7fd8;
  --blue-dark:#0f6bd0;
  --cyan:#18c7ef;
  --lime:#9ee01a;
  --yellow:#d7e21a;
  --green:#29c43a;
  --ink:#1f1f1f;
  --muted:#6b6b6b;
  --line:#d9d9d9;
  --soft:#f3f3f3;
  --white:#ffffff;
}
*{box-sizing:border-box;margin:0;padding:0}
html,body{width:1200px;height:3742px;overflow:hidden}
body{position:relative;font-family:"Open Sans",Arial,sans-serif;color:var(--ink);background:var(--white)}
.abs{position:absolute}
h1,h2,h3,.display{font-family:"Raleway","Open Sans",sans-serif}

/* hero */
.hero{left:0;top:0;width:1200px;height:640px}
.hero-bg{position:absolute;inset:0}
.brand{left:160px;top:22px;color:var(--white);font-family:"Raleway",sans-serif;font-weight:800;font-size:26px;letter-spacing:1px;display:flex;align-items:center;gap:8px}
.brand-dot{width:10px;height:10px;background:var(--white);border-radius:50%}
.nav{right:160px;top:30px;display:flex;gap:34px;font-size:12px;font-weight:600;color:var(--white);text-transform:uppercase}
.hero-kicker{left:160px;top:172px;color:var(--white);font-family:"Raleway",sans-serif;font-weight:600;font-size:22px;display:flex;align-items:center;gap:16px}
.hero-kicker::after{content:"";width:110px;height:2px;background:var(--white)}
.hero-title{left:160px;top:206px;color:var(--white);font-weight:800;font-size:38px;line-height:40px;width:520px}
.hero-tf{left:160px;top:312px;color:var(--white);font-weight:600;font-size:16px}
.hero-lead{left:160px;top:346px;width:300px;color:var(--white);font-size:14px;line-height:20px;border-left:2px solid rgba(255,255,255,.6);padding-left:10px}
.btn-outline{left:160px;top:416px;height:42px;width:195px;border-radius:21px;background:var(--white);display:flex;align-items:center;font-size:12px;font-weight:700;color:var(--ink);padding-left:26px;gap:30px}
.btn-outline .arrow{width:42px;height:42px;border-radius:50%;background:var(--magenta);display:flex;align-items:center;justify-content:center;margin-left:auto}
.slider-dots{left:1140px;top:255px;display:flex;flex-direction:column;align-items:center;gap:16px}
.slider-dots span{width:11px;height:11px;border:2px solid var(--white);border-radius:50%}
.slider-dots span.on{background:var(--white)}

/* form card */
.form-card{background:var(--white);box-shadow:0 8px 24px rgba(0,0,0,.18)}
.form-head{background:var(--blue-dark);color:var(--white);font-family:"Raleway",sans-serif;font-weight:700;font-size:15px;text-transform:uppercase;text-align:center;padding:12px 0;letter-spacing:.3px}
.form-body{padding:16px 25px 22px}
.field{border:1px solid var(--line);height:34px;margin-bottom:14px;font-size:12px;color:var(--muted);display:flex;align-items:center;padding-left:12px;gap:6px}
.field.focus{border-color:var(--blue);box-shadow:0 0 0 1px var(--blue)}
.field.area{height:86px;align-items:flex-start;padding-top:9px}
.btn-send{height:32px;border-radius:16px;background:linear-gradient(90deg,var(--blue),var(--cyan) 45%,var(--lime));color:var(--white);font-size:13px;font-weight:700;display:flex;align-items:center;justify-content:center}

/* intro */
.intro{left:0;top:560px;width:1200px;height:380px;background:var(--soft);z-index:-1}
.intro-line{left:0;width:1200px;text-align:center}
.intro-small{top:655px;font-size:16px;color:var(--muted)}
.intro-big{top:678px;font-size:25px;font-weight:700;font-family:"Raleway",sans-serif}
.intro-big em{font-style:normal;color:var(--blue)}
.intro-text{top:724px;font-size:16px;color:var(--muted);line-height:24px;width:700px;left:250px}
.intro-icons{left:0;top:790px;width:1200px;display:flex;justify-content:center;gap:40px}
.intro-icons span{width:88px;height:88px;border-radius:50%;box-shadow:0 4px 10px rgba(0,0,0,.15);display:flex;align-items:center;justify-content:center}

/* results */
.results-title{left:0;top:1005px;width:1200px;text-align:center;font-size:26px;font-weight:700;line-height:38px;text-transform:uppercase}
.blob-text{color:var(--white)}
.blob-text h3{font-size:28px;line-height:32px;font-weight:800}
.blob-text p{font-size:12px;margin-top:12px;line-height:17px;width:170px;opacity:.9}
.chart{background:var(--white);border:1px solid #e2e2e2;box-shadow:0 6px 20px rgba(0,0,0,.18);padding:12px 12px 0}
.chart-tab{display:inline-block;border:1px solid #ccc;border-bottom:none;font-size:11px;font-weight:700;padding:6px 9px;background:#f7f7f7}
.chart-menu{border-top:1px solid #ccc;border-bottom:1px solid #ccc;font-size:11px;padding:7px 4px;display:flex;gap:14px;color:var(--blue)}
.chart-menu b{color:var(--ink);font-weight:600;border-bottom:2px solid var(--blue)}
.chart-tools{display:flex;justify-content:space-between;align-items:center;margin-top:10px;font-size:10px}
.chart-tools .sel{border:1px solid #ccc;padding:3px 6px}
.chart-tools .vs{color:var(--blue)}
.seg{display:flex;border:1px solid #ccc}
.seg span{padding:3px 6px;border-left:1px solid #ccc}
.seg span:first-child{border-left:none}
.seg span.on{background:#ddd}
.legend{font-size:11px;margin:10px 0 0 4px;display:flex;align-items:center;gap:6px}
.legend i{width:9px;height:9px;border-radius:50%;background:var(--blue)}

/* testimonials */
.reviews-bg{left:0;top:2470px;width:1200px;height:1020px}
.reviews-title{left:0;top:2650px;width:1200px;text-align:center;color:var(--white);font-size:24px;font-weight:800;text-transform:uppercase}
.review{width:282px}
.review-card{background:var(--white);height:182px;padding:16px 20px;font-size:11px;line-height:18px;color:#555;position:relative}
.review-card::after{content:"";position:absolute;left:0;bottom:-18px;border-top:18px solid var(--white);border-right:18px solid transparent}
.review-card .quote{position:absolute;right:70px;bottom:10px;font-family:Georgia,serif;font-size:30px;color:#bbb}
.review-author{display:flex;align-items:center;gap:10px;margin-top:28px;color:var(--white)}
.avatar{width:56px;height:56px;border-radius:50%;border:3px solid var(--white);background:linear-gradient(135deg,#9a8a7a,#4a3c34);flex-shrink:0}
.review-author b{display:block;font-size:12px}
.review-author span{font-size:10px}
.chev{top:2810px;color:var(--white);font-size:30px}

/* contact */
.contact-left{left:160px;top:3105px;width:440px;height:350px;background:var(--blue-dark);color:var(--white);padding:40px 50px}
.contact-left h2{font-size:26px;line-height:30px;font-weight:700}
.contact-left p{font-size:12px;line-height:19px;margin-top:18px;opacity:.9}
.btn-ghost{display:inline-block;margin-top:24px;border:2px solid var(--white);border-radius:18px;padding:7px 24px;font-size:12px;font-weight:700}
.contact-form{left:600px;top:3105px;width:440px;height:350px}
.contact-form .form-head{background:var(--pink);padding:14px 0}
.contact-form .form-body{padding:14px 55px}

/* footer */
.footer-brand{left:160px;top:3528px;color:var(--blue);font-family:"Raleway",sans-serif;font-weight:800;font-size:30px;display:flex;align-items:center;gap:10px}
.footer-brand .sq{width:12px;height:12px;background:var(--lime)}
.footer-line{left:160px;top:3572px;width:200px;height:2px;background:var(--lime)}
.footer-contact{left:160px;top:3600px;font-size:13px;line-height:26px}
.footer-contact b{color:var(--blue)}
.footer-col{font-size:11px;line-height:30px;color:#444}
.socials{left:916px;top:3532px;display:flex;gap:10px}
.socials span{width:30px;height:30px;border-radius:50%;background:var(--blue)}
.socials span:nth-child(2){background:var(--white);border:2px solid var(--blue)}
.footer-bar{left:0;top:3697px;width:1200px;height:45px;background:var(--blue);color:var(--white);font-size:11px;display:flex;align-items:center;padding:0 160px}
</style>
</head>
<body>

<!-- HERO -->
<header class="abs hero">
  <svg class="hero-bg" width="1200" height="640" viewBox="0 0 1200 640" aria-hidden="true">
    <defs>
      <linearGradient id="heroGrad" x1="0" y1="0" x2="1" y2="0.3">
        <stop offset="0" stop-color="#5a16d8"/>
        <stop offset="0.5" stop-color="#a51bc4"/>
        <stop offset="1" stop-color="#f0136f"/>
      </linearGradient>
      <radialGradient id="heroGlow" cx="0.45" cy="0.3" r="0.35">
        <stop offset="0" stop-color="#ffffff" stop-opacity="0.18"/>
        <stop offset="1" stop-color="#ffffff" stop-opacity="0"/>
      </radialGradient>
    </defs>
    <path d="M0 0H1200V565C1050 600 900 560 720 520C520 480 300 500 0 610Z" fill="url(#heroGrad)"/>
    <circle cx="540" cy="190" r="230" fill="url(#heroGlow)"/>
  </svg>
  <div class="abs brand">BRIVOLTA<span class="brand-dot"></span></div>
  <nav class="abs nav"><span>Résultats</span><span>Références</span></nav>
  <div class="abs hero-kicker">BACKLINKS FRANÇAIS</div>
  <h1 class="abs hero-title">sur des magazines et blogs de qualité</h1>
  <div class="abs hero-tf">Trust Flow cible 15-2</div>
  <p class="abs hero-lead">Seuls les backlinks de qualité contribuent à augmenter votre trafic sur Quendo.</p>
  <a class="abs btn-outline">Voir les résultats
    <span class="arrow"><svg width="16" height="12" viewBox="0 0 16 12"><path d="M1 6H14M9 1L14 6L9 11" stroke="#fff" stroke-width="2" fill="none"/></svg></span>
  </a>
  <div class="abs slider-dots"><span></span><span class="on"></span><span></span></div>

  <form class="abs form-card" style="left:740px;top:168px;width:300px">
    <div class="form-head">Renseignements et tarifs</div>
    <div class="form-body">
      <div class="field focus">✉ Votre e-mail</div>
      <div class="field">⊕ Site web</div>
      <div class="field area">? Comment pouvons-nous vous aider ?</div>
      <div class="btn-send">Envoyer</div>
    </div>
  </form>
</header>

<!-- INTRO -->
<section class="abs intro"></section>
<p class="abs intro-line intro-small">Obtenez des backlinks sur des sites de qualité qui ont</p>
<h2 class="abs intro-line intro-big">un Trust <em>Flow élevé</em> et <em>augmentez votre trafic</em> sur Quendo.</h2>
<p class="abs intro-text" style="text-align:center">Nous supportons la plupart des thématiques et rédigeons les articles. Aucun lien retour nécessaire. Sans engagement.</p>
<div class="abs intro-icons">
  <span style="background:#f7941d">
    <svg width="40" height="40" viewBox="0 0 40 40"><g fill="none" stroke="#fff" stroke-width="4" stroke-linecap="round"><path d="M17 23L23 17"/><path d="M14 20L10 24A5 5 0 0 0 17 31L21 27"/><path d="M26 20L30 16A5 5 0 0 0 23 9L19 13"/></g></svg>
  </span>
  <span style="background:#17a7e8">
    <svg width="44" height="44" viewBox="0 0 44 44"><circle cx="22" cy="22" r="15" fill="none" stroke="#fff" stroke-width="3"/><rect x="4" y="18" width="36" height="9" fill="#fff"/><text x="22" y="25.5" font-size="7.5" font-weight="700" text-anchor="middle" fill="#17a7e8" font-family="Open Sans,sans-serif">WWW</text></svg>
  </span>
  <span style="background:#8cc63f"><svg width="30" height="30"><circle cx="15" cy="15" r="11" fill="#fff"/></svg></span>
</div>

<!-- RESULTS -->
<h2 class="abs results-title">Exemples de résultats obtenus<br>avec nos backlinks</h2>

<svg class="abs" style="left:0;top:1135px" width="470" height="380" viewBox="0 0 470 380" aria-hidden="true">
  <defs><linearGradient id="blobA" x1="0" y1="1" x2="1" y2="0"><stop offset="0" stop-color="#d7e21a"/><stop offset="1" stop-color="#18b84a"/></linearGradient></defs>
  <path d="M0 10C80 -5 170 10 230 25C300 40 360 30 410 70C470 115 440 175 400 215C370 250 385 300 330 330C250 375 150 330 70 360C40 372 15 378 0 380Z" fill="url(#blobA)"/>
</svg>
<div class="abs blob-text" style="left:115px;top:1278px"><h3>De 0 à 26 000<br>visites/mois</h3><p>Et ça continue d'augmenter !</p></div>

<div class="abs chart" style="left:520px;top:1155px;width:655px;height:340px">
  <span class="chart-tab">Explorer</span>
  <div class="chart-menu"><b>Summary</b><span>Site Usage</span><span>Ecommerce</span><span>Revenus</span></div>
  <div class="chart-tools"><div><span class="sel">Sessions ▾</span> VS. <span class="vs">Select a metric</span></div><div class="seg"><span>Day</span><span>Week</span><span class="on">Month</span></div></div>
  <div class="legend"><i></i>Sessions</div>
  <svg width="630" height="200" viewBox="0 0 630 200" font-size="9" font-family="Open Sans,sans-serif" fill="#555">
    <line x1="10" y1="22" x2="625" y2="22" stroke="#eee"/><line x1="10" y1="82" x2="625" y2="82" stroke="#eee"/><line x1="10" y1="165" x2="625" y2="165" stroke="#ccc"/>
    <text x="12" y="18">30,000</text><text x="12" y="78">15,000</text>
    <path d="M12 163L50 163L88 162L126 161L164 158L202 122L240 100L278 116L316 120L354 121L392 124L430 124L468 126L506 121L544 119L582 108L620 68L620 165L12 165Z" fill="#dbe9f6"/>
    <polyline points="12,163 50,163 88,162 126,161 164,158 202,122 240,100 278,116 316,120 354,121 392,124 430,124 468,126 506,121 544,119 582,108 620,68" fill="none" stroke="#1a73c8" stroke-width="2.5"/>
    <g fill="#1a73c8"><circle cx="12" cy="163" r="3"/><circle cx="88" cy="162" r="3"/><circle cx="164" cy="158" r="3"/><circle cx="240" cy="100" r="3"/><circle cx="316" cy="120" r="3"/><circle cx="392" cy="124" r="3"/><circle cx="468" cy="126" r="3"/><circle cx="544" cy="119" r="3"/><circle cx="620" cy="68" r="3"/></g>
    <text x="10" y="182">April 2017</text><text x="130" y="182">July 2017</text><text x="240" y="182">October 2017</text><text x="370" y="182">January 2018</text><text x="495" y="182">April 2018</text><text x="585" y="182">July 2018</text>
  </svg>
</div>

<svg class="abs" style="left:730px;top:1585px" width="470" height="380" viewBox="0 0 470 380" aria-hidden="true">
  <defs><linearGradient id="blobB" x1="0" y1="0" x2="1" y2="1"><stop offset="0" stop-color="#d23ff0"/><stop offset="1" stop-color="#f0136f"/></linearGradient></defs>
  <path d="M470 0C390 5 310 -5 230 20C140 45 60 30 20 90C-10 140 40 180 60 220C90 270 40 320 120 350C200 380 300 340 380 360C420 370 450 375 470 378Z" fill="url(#blobB)"/>
</svg>
<div class="abs blob-text" style="left:875px;top:1710px"><h3>De 1 200 à 4 400<br>visites/mois</h3><p>Le trafic en provenance de Quendo a plus que triplé en 12 mois.</p></div>

<div class="abs chart" style="left:28px;top:1600px;width:657px;height:350px">
  <span class="chart-tab">Explorer</span>
  <div class="chart-menu"><b>Summary</b><span>Site Usage</span><span>Goal Set 1</span><span>Goal Set 2</span><span>Goal Set 3</span><span>Ecommerce</span></div>
  <div class="chart-tools"><div><span class="sel">Sessions ▾</span> VS. <span class="vs">Select a metric</span></div><div class="seg"><span>Day</span><span>Week</span><span class="on">Month</span></div></div>
  <div class="legend"><i></i>Sessions</div>
  <svg width="630" height="210" viewBox="0 0 630 210" font-size="9" font-family="Open Sans,sans-serif" fill="#555">
    <line x1="10" y1="20" x2="625" y2="20" stroke="#eee"/><line x1="10" y1="95" x2="625" y2="95" stroke="#eee"/><line x1="10" y1="175" x2="625" y2="175" stroke="#ccc"/>
    <text x="12" y="16">5,000</text><text x="12" y="91">2,500</text>
    <path d="M12 128L55 126L98 126L141 125L184 116L227 85L270 83L313 83L356 80L399 50L442 76L485 65L528 70L571 65L614 55L614 175L12 175Z" fill="#dbe9f6"/>
    <polyline points="12,128 55,126 98,126 141,125 184,116 227,85 270,83 313,83 356,80 399,50 442,76 485,65 528,70 571,65 614,55" fill="none" stroke="#1a73c8" stroke-width="2.5"/>
    <g fill="#1a73c8"><circle cx="12" cy="128" r="3"/><circle cx="55" cy="126" r="3"/><circle cx="98" cy="126" r="3"/><circle cx="141" cy="125" r="3"/><circle cx="184" cy="116" r="3"/><circle cx="227" cy="85" r="3"/><circle cx="270" cy="83" r="3"/><circle cx="313" cy="83" r="3"/><circle cx="356" cy="80" r="3"/><circle cx="399" cy="50" r="3"/><circle cx="442" cy="76" r="3"/><circle cx="485" cy="65" r="3"/><circle cx="528" cy="70" r="3"/><circle cx="571" cy="65" r="3"/><circle cx="614" cy="55" r="3"/></g>
    <text x="100" y="192">July 2017</text><text x="245" y="192">October 2017</text><text x="390" y="192">January 2018</text><text x="545" y="192">April 2018</text>
  </svg>
</div>

<svg class="abs" style="left:0;top:1968px" width="440" height="445" viewBox="0 0 440 445" aria-hidden="true">
  <defs><linearGradient id="blobC" x1="0" y1="0" x2="1" y2="1"><stop offset="0" stop-color="#1a3ef0"/><stop offset="1" stop-color="#18c7ef"/></linearGradient></defs>
  <path d="M0 0C100 10 220 20 300 50C380 80 400 130 370 175C340 220 430 260 400 330C370 400 260 390 160 410C90 425 40 440 0 445Z" fill="url(#blobC)"/>
</svg>
<div class="abs blob-text" style="left:115px;top:2170px"><h3>De 0 à 60 000<br>visites/semaine</h3><p>C'est plus de 240 000 visites par mois pour ce site.</p></div>

<div class="abs chart" style="left:520px;top:2055px;width:655px;height:340px">
  <span class="chart-tab">Explorer</span>
  <div class="chart-menu"><b>Summary</b><span>Site Usage</span><span>Ecommerce</span><span>Revenus</span></div>
  <div class="chart-tools"><div><span class="sel">Sessions ▾</span> VS. <span class="vs">Select a metric</span></div><div class="seg"><span>Day</span><span class="on">Week</span><span>Month</span></div></div>
  <div class="legend"><i></i>Sessions</div>
  <svg width="630" height="200" viewBox="0 0 630 200" font-size="9" font-family="Open Sans,sans-serif" fill="#555">
    <line x1="10" y1="12" x2="625" y2="12" stroke="#eee"/><line x1="10" y1="90" x2="625" y2="90" stroke="#eee"/><line x1="10" y1="165" x2="625" y2="165" stroke="#ccc"/>
    <text x="12" y="10">100,000</text><text x="12" y="86">50,000</text>
    <path d="M12 164L60 164L110 164L150 162L180 150L200 130L220 105L240 98L260 92L280 96L300 82L320 88L340 76L360 84L380 70L400 90L420 82L440 94L460 100L480 88L500 80L520 90L540 76L560 70L580 86L600 76L620 78L620 165L12 165Z" fill="#dbe9f6"/>
    <polyline points="12,164 60,164 110,164 150,162 180,150 200,130 220,105 240,98 260,92 280,96 300,82 320,88 340,76 360,84 380,70 400,90 420,82 440,94 460,100 480,88 500,80 520,90 540,76 560,70 580,86 600,76 620,78" fill="none" stroke="#1a73c8" stroke-width="2"/>
    <text x="20" y="182">July 2017</text><text x="150" y="182">October 2017</text><text x="280" y="182">January 2018</text><text x="420" y="182">April 2018</text><text x="570" y="182">July 2018</text>
  </svg>
</div>

<!-- TESTIMONIALS -->
<svg class="abs reviews-bg" width="1200" height="1020" viewBox="0 0 1200 1020" aria-hidden="true">
  <defs><linearGradient id="revGrad" x1="0" y1="0" x2="1" y2="0.2"><stop offset="0" stop-color="#5a16d8"/><stop offset="0.5" stop-color="#a51bc4"/><stop offset="1" stop-color="#f0136f"/></linearGradient></defs>
  <path d="M0 50C300 60 500 10 800 30C1000 42 1100 20 1200 0V840C1100 900 900 960 700 920C500 880 250 890 0 940Z" fill="url(#revGrad)"/>
</svg>
<h2 class="abs reviews-title">Voici ce qu'en pensent nos clients</h2>
<span class="abs chev" style="left:88px">‹</span>
<span class="abs chev" style="left:1092px">›</span>

<article class="abs review" style="left:160px;top:2735px">
  <div class="review-card">En quelques mois, nous sommes passés en 1ère page de Quendo pour tous les mots-clés ciblés. L'agence est très professionnelle et travaille de manière méthodique. Les rapports qu'ils nous envoient chaque mois sont simples à comprendre et permettent de suivre l'avancement du projet.<span class="quote">”</span></div>
  <div class="review-author"><div class="avatar" role="img" aria-label="Photo du client Mathis Lefranc"></div><div><b>Mathis Lefranc</b><span>Propriétaire - Clairvue Média</span></div></div>
</article>
<article class="abs review" style="left:460px;top:2735px">
  <div class="review-card">Grâce à leur travail, les pages importantes de mon site sont maintenant bien visibles dans les premiers résultats de recherche de Quendo pour des mots-clés compétitifs et importants pour mon agence de voyage. Ils sont accessibles et répondent à toutes mes questions rapidement.<span class="quote">”</span></div>
  <div class="review-author"><div class="avatar" role="img" aria-label="Photo du client Lucien Barjot"></div><div><b>Lucien Barjot</b><span>Propriétaire - Azuline Voyages</span></div></div>
</article>
<article class="abs review" style="left:760px;top:2735px">
  <div class="review-card">Ils ont piloté des campagnes de netlinking pour notre boutique en ligne qui ont permis de mettre la main sur plus de 90 liens de qualité et d'améliorer le positionnement global du site sur Quendo.<span class="quote">”</span></div>
  <div class="review-author"><div class="avatar" role="img" aria-label="Photo du client Fabien Orsoni"></div><div><b>Fabien Orsoni</b><span>Propriétaire - Atelier Perlane</span></div></div>
</article>

<!-- CONTACT -->
<section class="abs contact-left">
  <h2>Demande de renseignements</h2>
  <p>Vous aimeriez avoir plus de renseignements ou connaître les tarifs ? Remplissez le court formulaire de prise de contact et parlez-nous de vos besoins et de vos objectifs SEO. Les tarifs des backlinks varient selon la thématique.</p>
  <span class="btn-ghost">Nous contacter</span>
</section>
<form class="abs form-card contact-form">
  <div class="form-head">Renseignements et tarifs</div>
  <div class="form-body">
    <div class="field focus">✉ Votre e-mail</div>
    <div class="field">⊕ Site web</div>
    <div class="field area" style="height:100px">? Comment pouvons-nous vous aider ?</div>
    <div class="btn-send">Envoyer</div>
  </div>
</form>

<!-- FOOTER -->
<footer>
  <div class="abs footer-brand">BRIVOLTA<span class="sq"></span></div>
  <div class="abs footer-line"></div>
  <div class="abs footer-contact"><b>☎ Call : +(123) 5550 142</b><br>✉ info@brivolta.com</div>
  <div class="abs footer-col" style="left:462px;top:3522px">Accueil<br>Améliorer son SEO<br>Mon compte</div>
  <div class="abs footer-col" style="left:702px;top:3522px">Mentions légales<br>À propos<br>Contact</div>
  <div class="abs socials"><span></span><span></span><span></span></div>
  <div class="abs footer-bar">© 2018 Brivolta. All rights reserved.</div>
</footer>

</body>
</html>
```